Business Card Design Project

Create an impressive business care to use
Updates

My logo is available at http://corvalune.example, or

Industry/Entity Type

Business

Requirements
Must have
• company logo

```html
<!DOCTYPE html>
<html lang="en">
<head>
<meta charset="utf-8">
<title>Corvalune Business Card</title>
<link rel="stylesheet" href="https://fonts.googleapis.com/css2?family=Questrial&family=PT+Sans:wght@400&display=swap">
<style>
  :root {
    --bg: #ebe8e6;
    --paper: #f7f7f5;
    --sky: #2aa8df;
    --leaf: #8cbf3f;
    --sun: #f2a531;
    --ink: #1c1c1c;
    --rule: #6d6d6d;
  }
  * { margin: 0; padding: 0; box-sizing: border-box; }
  html, body { width: 1200px; height: 960px; overflow: hidden; }
  body {
    background: var(--bg);
    position: relative;
    font-family: "PT Sans", sans-serif;
    color: var(--ink);
  }
  .card {
    position: absolute;
    width: 560px;
    height: 320px;
    background: var(--paper);
    overflow: hidden;
    box-shadow: 0 6px 18px rgba(0,0,0,0.12);
  }
  .card--back { left: 70px; top: 150px; }
  .card--front { left: 570px; top: 490px; }
  .card__band {
    position: absolute;
    left: 0; top: 0; bottom: 0;
    background: var(--sky);
  }
  .card--back .card__band { width: 170px; }
  .card--front .card__band { width: 205px; }
  .card__decor {
    position: absolute;
    right: 0; top: 0;
    width: 160px;
    height: 125px;
    background: linear-gradient(135deg, var(--leaf) 0%, var(--sky) 55%, var(--sun) 100%);
    opacity: 0.85;
  }
  .card__mark {
    position: absolute;
    left: 180px; top: 52px;
    width: 22px; height: 22px;
    border-radius: 50%;
    background: var(--leaf);
  }
  .identity {
    position: absolute;
    left: 212px; top: 40px;
    font-family: "Questrial", sans-serif;
    font-size: 15px;
    line-height: 1.35;
    letter-spacing: 0.5px;
  }
  .identity .role { font-size: 13px; }
  .divider {
    position: absolute;
    height: 1px;
    background: var(--rule);
  }
  .divider::after {
    content: "";
    position: absolute;
    right: -2px; top: -3px;
    border-left: 4px solid transparent;
    border-right: 4px solid transparent;
    border-top: 6px solid var(--rule);
  }
  .divider--a { left: 180px; top: 118px; width: 200px; }
  .divider--b { left: 40px; top: 168px; width: 220px; }
  .divider--c { left: 290px; top: 168px; width: 230px; }
  .office {
    position: absolute;
    font-size: 10px;
    line-height: 1.65;
    font-style: normal;
  }
  .office--us { left: 40px; top: 182px; }
  .office--cn { left: 290px; top: 182px; }
  .wordmark {
    position: absolute;
    left: 110px; top: 150px;
    font-family: "Questrial", sans-serif;
    font-size: 48px;
    letter-spacing: 7px;
    color: var(--ink);
  }
</style>
</head>
<body>

  <section class="card card--back" aria-label="Business card back">
    <div class="card__band"></div>
    <div class="card__decor" role="img" aria-label="Decorative sweeping arcs in green, blue and orange"></div>
    <div class="card__mark"></div>
    <div class="identity">
      <div class="name">Marcus Lin Tao, PhD</div>
      <div class="name-cn">陶林 博士</div>
      <div class="role">CEO</div>
    </div>
    <div class="divider divider--a"></div>
    <div class="divider divider--b"></div>
    <div class="divider divider--c"></div>
    <address class="office office--us">
      U.S.<br>
      2480 Harbor Ridge Ave, Suite 210<br>
      Portland, OR 97201<br>
      Email: mtao@corvalune.example<br>
      Cell: 555-014-2290<br>
      www.corvalune.example
    </address>
    <address class="office office--cn">
      China<br>
      1807, No.9 Lantern Road, Riverside District,<br>
      Hangzhou, China 310000<br>
      杭州市滨江区灯笼路9号1807室<br>
      www.northvale.example
    </address>
  </section>

  <section class="card card--front" aria-label="Business card front">
    <div class="card__band"></div>
    <div class="card__decor" role="img" aria-label="Decorative sweeping arcs in green, blue and orange"></div>
    <div class="wordmark">CORVALUNE</div>
  </section>

</body>
</html>
```